LVP Roofing- Bold Web Design Project

We need a website design for a company that constructs and repairs commercial and residential roofing. They need a website design that looks clean, cutting edge, and can keep up with their competitors websites (Norvelle Crest, Fenwright Roofing Company, TZL Construction). They want to look experienced and "big" enough to handle large commercial projects. They also are striving for a professional and educational feel, and want to really articulate that they work with both residential/HOA and commercial clientele. They want a high conversion rate to their social media platforms and to another area of the site where they can fill out a form, so those areas should be emphasized.

Target Market(s)

Men and Women mainly between 25 and 65, typically in the higher income bracket (200,000+).

Industry/Entity Type

Residential

Requirements
Must have
• Landing page must have two separate but equally prominent buttons, directing the customers to a specific area of the site based on their need: commercial or residential. Clicking ether of these links will lead them to a welcome page for residential customers, or a welcome page for commercial clients.
-So must have 2 pages, a landing page and a welcome page that can be adapted for use as the commercial page and the residential page.
- A photo slider on the landing page
Nice to have
• -Color scheme should generally follow along with the colors used in the logo
-Professional, bold and modern.
Should not have
• -Avoid the "mom and pop" look
-Avoid the color red in the color scheme

```html
<!DOCTYPE html>
<html lang="en">
<head>
<meta charset="utf-8">
<title>LVP Roofing – Construction &amp; Disaster Management</title>
<link href="https://fonts.googleapis.com/css2?family=PT+Sans:wght@400;700&display=swap" rel="stylesheet">
<style>
:root{
  --green:#7fa91d;
  --green-light:#9cc52f;
  --green-dark:#5f8311;
  --footer:#6c9116;
  --footer-dark:#5c7d10;
  --ink:#2b2b2b;
  --body:#555;
  --muted:#777;
  --line:#dcdcdc;
  --panel:#f4f4f4;
  --white:#fff;
}
*{box-sizing:border-box;margin:0;padding:0}
html,body{width:960px;height:1200px;overflow:hidden;background:var(--white)}
body{position:relative;font-family:Arial,Helvetica,sans-serif;color:var(--body)}
.abs{position:absolute}
.head-font{font-family:"PT Sans",sans-serif}

/* header */
.brand{left:97px;top:36px;color:var(--ink);font-family:"PT Sans",sans-serif}
.brand-name{font-size:30px;font-weight:700;letter-spacing:1px;line-height:1}
.brand-tag{font-size:6.5px;color:#444;letter-spacing:.3px;margin-top:6px;text-transform:uppercase}
.contractor{left:537px;top:56px;display:flex;align-items:center;gap:8px;font-family:"PT Sans",sans-serif;font-size:12px;color:var(--ink)}
.head-divider{left:695px;top:38px;width:1px;height:54px;background:var(--line)}
.call{left:721px;top:43px;font-family:"PT Sans",sans-serif;font-size:10px;color:var(--ink)}
.call em{font-style:normal;color:var(--green)}
.phone{left:714px;top:59px;display:flex;align-items:center;gap:5px;font-family:"PT Sans",sans-serif;font-weight:700;font-size:19.5px;color:var(--ink)}

/* nav */
.nav{left:0;top:111px;width:960px;height:35px;background:linear-gradient(var(--green-light),var(--green));display:flex;padding-left:82px}
.nav a{display:flex;align-items:center;justify-content:center;height:35px;color:var(--white);text-decoration:none;font-family:"PT Sans",sans-serif;font-size:12.5px;border-right:1px solid rgba(255,255,255,.25)}
.nav a.active{background:linear-gradient(#8aae2a,#6b9217)}

/* hero */
.hero{left:0;top:146px;width:960px;height:284px;background:linear-gradient(90deg,#7a8a5c 0%,#5c5a50 30%,#4a4640 55%,#2d2b27 80%,#1f1e1b 100%)}
.hero-title{left:611px;top:175px;color:var(--white);font-family:"PT Sans",sans-serif;font-size:15px;font-weight:700;line-height:20px}
.hero-list{left:613px;top:246px;list-style:none;color:#ddd;font-family:"PT Sans",sans-serif;font-size:10.5px}
.hero-list li{display:flex;align-items:center;gap:8px;height:23.3px}
.btn{display:flex;align-items:center;justify-content:space-between;color:var(--white);font-family:"PT Sans",sans-serif;font-weight:700;background:linear-gradient(#94bf2c,#628c12);border-radius:3px;padding:0 10px 0 14px}
.hero-btn{left:616px;top:364px;width:126px;height:31px;font-size:14.5px}
.pointer{left:110px;top:408px}

/* audience strip */
.strip{left:0;top:430px;width:960px;height:95px;background:linear-gradient(#f2f2f2,#e3e3e3)}
.audience{top:430px;height:95px;border-left:1px solid #cfcfcf;border-right:1px solid #cfcfcf;background:linear-gradient(#f8f8f8,#e6e6e6)}
.audience.commercial{left:82px;width:402px}
.audience.residential{left:485px;width:388px;background:linear-gradient(#f4f4f4,#e9e9e9)}
.aud-icon{position:absolute;left:26px;top:21px;width:44px;height:40px;border-radius:4px}
.aud-title{position:absolute;left:91px;top:19px;font-family:"PT Sans",sans-serif;font-size:20px;color:var(--ink)}
.aud-text{position:absolute;left:92px;top:43px;width:280px;font-size:10px;line-height:11.5px;color:#333}

/* info boxes */
.info{left:107px;top:551px;width:486px;height:97px;border:1px solid #eee;background:linear-gradient(#fff,#f1f1f1);display:flex}
.info>div{border-right:1px solid #e3e3e3;height:100%;position:relative}
.info>div:last-child{border-right:0}
.cell-badge{width:151px}
.cell-weather{width:168px}
.cell-county{flex:1}
.badge-shape{position:absolute;left:18px;top:18px;width:110px;height:58px;background:linear-gradient(#c9c9c9,#9a9a9a);clip-path:polygon(50% 0,100% 28%,100% 100%,0 100%,0 28%)}
.weather-icon{position:absolute;left:13px;top:22px;width:38px;height:30px;border-radius:50%;background:radial-gradient(circle at 55% 40%,#f7c52c 0 35%,#d9e1ea 36% 100%)}
.w-title{position:absolute;left:63px;top:21px;font-family:"PT Sans",sans-serif;font-size:11px;font-weight:700;color:var(--ink)}
.w-temp{position:absolute;left:63px;top:37px;font-size:9px;font-weight:700;color:#333}
.w-place{position:absolute;left:63px;top:48px;font-size:10px;color:#666}
.w-next{position:absolute;left:63px;top:68px;width:58px;height:13px;border-radius:2px;background:linear-gradient(#e6e6e6,#cfcfcf);font-size:7.5px;color:#888;display:flex;align-items:center;justify-content:center;gap:6px}
.c-title{position:absolute;left:14px;top:14px;font-family:"PT Sans",sans-serif;font-size:14.5px;line-height:16px;color:var(--ink)}
.c-text{position:absolute;left:14px;top:50px;width:135px;font-size:9px;line-height:11px;color:#888}
.c-text a{color:var(--green)}

/* about */
.about-title{left:110px;top:678px;font-family:"PT Sans",sans-serif;font-size:15px;color:var(--ink)}
.about-text{left:110px;top:698px;width:470px;font-size:9.6px;line-height:11.5px;color:#666}
.points{left:110px;top:740px;width:475px;list-style:none}
.points li{position:relative;padding-left:21px;margin-bottom:10px}
.points li svg{position:absolute;left:0;top:0}
.points h3{font-family:"PT Sans",sans-serif;font-size:11px;font-weight:700;color:var(--ink);margin-bottom:2px}
.points p{font-size:9.3px;line-height:11.6px;color:#777}

/* sidebar form */
.form-tab{left:616px;top:551px;width:241px;height:29px;background:linear-gradient(#97c12d,#6f9a17);color:var(--white);font-family:"PT Sans",sans-serif;font-weight:700;font-size:14px;display:flex;align-items:center;padding-left:9px}
.form-box{left:623px;top:580px;width:226px;height:224px;border:1px solid #e3e3e3;background:var(--white)}
.field{position:absolute;left:17px;width:190px;height:25px;border:1px solid #d6d6d6;font-size:9.5px;color:#555;display:flex;align-items:center;padding-left:8px}
.form-label{position:absolute;left:17px;top:119px;font-size:9.5px;font-weight:700;color:#444}
.select-arrow{position:absolute;right:-1px;top:-1px;width:27px;height:25px;background:linear-gradient(#8fb92a,#6c9614);display:flex;align-items:center;justify-content:center}
.form-btn{left:672px;top:756px;width:125px;height:31px;font-size:14.5px}

/* testimonials */
.t-title{left:618px;top:822px;font-family:"PT Sans",sans-serif;font-size:15px;color:var(--ink)}
.t-box{left:616px;top:847px;width:241px;height:71px;background:#f3f3f3;border-radius:3px;padding:9px 10px}
.t-box p{font-size:9.3px;line-height:11.5px;color:#666}
.t-author{margin-top:5px;font-size:9.5px;font-style:italic;color:var(--green)}
.t-author b{font-style:normal}
.t-tail{left:637px;top:918px}

/* footer */
.footer{left:0;top:1016px;width:960px;height:184px;background:var(--footer)}
.foot-contact{left:121px;top:1074px;font-family:"PT Sans",sans-serif;font-size:9.5px;line-height:11.5px;color:var(--white)}
.foot-contact i{font-style:italic}
.foot-divider{left:448px;top:1048px;width:1px;height:97px;background:rgba(0,0,0,.15);box-shadow:1px 0 0 rgba(255,255,255,.1)}
.foot-badge{left:480px;top:1062px;width:56px;height:58px;background:linear-gradient(#e8e8e8,#bdbdbd);clip-path:polygon(0 0,100% 0,100% 62%,50% 100%,0 62%)}
.foot-note{left:565px;top:1071px;font-family:"PT Sans",sans-serif;font-size:14.5px;line-height:18px;color:var(--white)}
.copyright{left:0;top:1178px;width:960px;height:22px;background:var(--footer-dark);border-top:1px solid rgba(255,255,255,.15);color:var(--white);font-size:8px;display:flex;align-items:center;justify-content:center}
</style>
</head>
<body>

<header>
  <div class="abs brand">
    <div class="brand-name">LVP NETWORK</div>
    <div class="brand-tag">Construction &amp; Disaster Management</div>
  </div>
  <div class="abs contractor">
    <svg width="24" height="18" viewBox="0 0 24 18"><path d="M2 14 A10 10 0 0 1 22 14 Z" fill="#f3c01c"/><rect x="0" y="13" width="24" height="4" rx="2" fill="#e3a90e"/></svg>
    Full Service Contractor
  </div>
  <div class="abs head-divider"></div>
  <div class="abs call">Call today for a <em>FREE</em> estimate!</div>
  <div class="abs phone">
    <svg width="17" height="17" viewBox="0 0 17 17"><circle cx="8.5" cy="8.5" r="8" fill="#8cb523"/><path d="M4 7 Q8.5 3 13 7 L12 8.5 L10 7.5 L7 7.5 L5 8.5 Z M5.5 9 h6 v3.5 h-6z" fill="#fff"/></svg>
    (555) 201-4870
  </div>
</header>

<nav class="abs nav">
  <a class="active" style="width:82px">Home</a>
  <a style="width:99px">About Us</a>
  <a style="width:97px">Services</a>
  <a style="width:189px">Insurance &amp; Storm Damage</a>
  <a style="width:106px">Ventilation</a>
  <a style="width:97px">Products</a>
  <a style="width:108px;border-right:0">Contact Us</a>
</nav>

<section>
  <div class="abs hero" role="img" aria-label="Photo slider: two-storey house with grey siding, gabled roof and stone chimney among green trees"></div>
  <h1 class="abs hero-title">Construction &amp; Disaster<br>Management for Commercial</h1>
  <ul class="abs hero-list">
    <li><svg width="13" height="13"><circle cx="6.5" cy="6.5" r="6.5" fill="#8cb523"/><path d="M3.5 6.8 L5.8 9 L9.7 4.6" stroke="#fff" stroke-width="1.6" fill="none"/></svg>Cellar Membrane Waterproofing</li>
    <li><svg width="13" height="13"><circle cx="6.5" cy="6.5" r="6.5" fill="#8cb523"/><path d="M3.5 6.8 L5.8 9 L9.7 4.6" stroke="#fff" stroke-width="1.6" fill="none"/></svg>Commercial Roofing</li>
    <li><svg width="13" height="13"><circle cx="6.5" cy="6.5" r="6.5" fill="#8cb523"/><path d="M3.5 6.8 L5.8 9 L9.7 4.6" stroke="#fff" stroke-width="1.6" fill="none"/></svg>Conservatory Roof</li>
    <li><svg width="13" height="13"><circle cx="6.5" cy="6.5" r="6.5" fill="#8cb523"/><path d="M3.5 6.8 L5.8 9 L9.7 4.6" stroke="#fff" stroke-width="1.6" fill="none"/></svg>Conservatory Roof Seals</li>
  </ul>
  <a class="abs btn hero-btn">Readmore
    <svg width="20" height="20"><circle cx="10" cy="10" r="10" fill="#4a6a0c"/><path d="M8 6 L13.5 10 L8 14 Z" fill="#fff"/></svg>
  </a>
  <svg class="abs pointer" width="38" height="22"><path d="M0 22 L19 0 L38 22 Z" fill="#f5f5f5"/></svg>
</section>

<section>
  <div class="abs strip"></div>
  <div class="abs audience commercial">
    <div class="aud-icon" role="img" aria-label="Bank building icon" style="background:linear-gradient(#d8dde2,#8c959e)"></div>
    <h2 class="aud-title">LVP COMMERCIAL</h2>
    <p class="aud-text">Lorem ipsum dolor sit amet, consectetuer adipiscing elit, sed diam nonummy nibh euismod tincidunt ut laoreet dolore magna aliquam erat volutpat.</p>
  </div>
  <div class="abs audience residential">
    <div class="aud-icon" role="img" aria-label="Map with location pin icon" style="left:20px;background:linear-gradient(135deg,#8fc64a,#4e95d6)"></div>
    <h2 class="aud-title" style="left:88px">LVP RESIDENTAL</h2>
    <p class="aud-text" style="left:89px;width:275px">Lorem ipsum dolor sit amet, consectetuer adipiscing elit, sed diam nonummy nibh euismod tincidunt ut laoreet dolore magna aliquam erat volutpat.</p>
  </div>
</section>

<section class="abs info">
  <div class="cell-badge"><div class="badge-shape" role="img" aria-label="Roofing contractor certification badge"></div></div>
  <div class="cell-weather">
    <div class="weather-icon" role="img" aria-label="Sun behind cloud"></div>
    <div class="w-title">Current Weather</div>
    <div class="w-temp">11° c</div>
    <div class="w-place">Liberty, Kansas City</div>
    <div class="w-next">Next Area <svg width="5" height="6"><path d="M0 0 L5 3 L0 6Z" fill="#666"/></svg></div>
  </div>
  <div class="cell-county">
    <div class="c-title">Johnson County<br>Licensed Contractor</div>
    <p class="c-text">Lorem ipsum dolor sit amet, consectetuer adipiscing elit, sed diam. <a>Readmore</a></p>
  </div>
</section>

<section>
  <h2 class="abs about-title">LVP Roofing &amp; Construction</h2>
  <p class="abs about-text">LVP Roofing was founded on the principles of honesty and integrity. We have many years of building experience – including new construction and home remodel, with a primary focus on roofing and siding.</p>
  <ul class="abs points">
    <li><svg width="13" height="13"><circle cx="6.5" cy="6.5" r="6.5" fill="#8cb523"/><path d="M3.5 6.8 L5.8 9 L9.7 4.6" stroke="#fff" stroke-width="1.6" fill="none"/></svg>
      <h3>Full Service Contractor</h3>
      <p>Lorem ipsum dolor sit amet, consectetur adipisicing elit, sed do eiusmod tempor incididunt ut labore et dolore magna aliqua.</p></li>
    <li><svg width="13" height="13"><circle cx="6.5" cy="6.5" r="6.5" fill="#8cb523"/><path d="M3.5 6.8 L5.8 9 L9.7 4.6" stroke="#fff" stroke-width="1.6" fill="none"/></svg>
      <h3>We answer the phone!</h3>
      <p>Sed ut perspiciatis unde omnis iste natus error sit voluptatem accusantium doloremque laudantium, totam rem aperiam, eaque ipsa quae ab illo inventore veritatis et quasi architecto beatae vitae dicta sunt explicabo.</p></li>
    <li><svg width="13" height="13"><circle cx="6.5" cy="6.5" r="6.5" fill="#8cb523"/><path d="M3.5 6.8 L5.8 9 L9.7 4.6" stroke="#fff" stroke-width="1.6" fill="none"/></svg>
      <h3>Storm Damage Specialist</h3>
      <p>Nemo enim ipsam voluptatem quia voluptas sit aspernatur aut odit aut fugit, sed quia consequuntur magni dolores eos qui ratione voluptatem sequi nesciunt.</p></li>
    <li><svg width="13" height="13"><circle cx="6.5" cy="6.5" r="6.5" fill="#8cb523"/><path d="M3.5 6.8 L5.8 9 L9.7 4.6" stroke="#fff" stroke-width="1.6" fill="none"/></svg>
      <h3>Assistance with your insurance claim process</h3>
      <p>Neque porro quisquam est, qui dolorem ipsum quia dolor sit amet, consectetur, adipisci velit, sed quia non numquam eius modi tempora incidunt ut labore et dolore magnam aliquam quaerat voluptatem.</p></li>
  </ul>
</section>

<aside>
  <div class="abs form-tab">Serving the greater Kansas City area</div>
  <form class="abs form-box">
    <div class="field" style="top:18px">First Name</div>
    <div class="field" style="top:50px">Last Name</div>
    <div class="field" style="top:82px">E-mail</div>
    <div class="form-label">Location</div>
    <div class="field" style="top:134px">Gladstone
      <span class="select-arrow"><svg width="8" height="5"><path d="M0 0 H8 L4 5Z" fill="#fff"/></svg></span>
    </div>
  </form>
  <a class="abs btn form-btn">Confirmed
    <svg width="20" height="20"><circle cx="10" cy="10" r="10" fill="#4a6a0c"/><path d="M8 6 L13.5 10 L8 14 Z" fill="#fff"/></svg>
  </a>

  <h2 class="abs t-title">Testimonials</h2>
  <blockquote class="abs t-box">
    <p>Lorem ipsum dolor sit amet, consectetur adipisicing elit, sed do eiusmod tempor incididunt ut labore et dolore magna aliqua.</p>
    <div class="t-author">Daniel, <b>Smithville</b></div>
  </blockquote>
  <svg class="abs t-tail" width="16" height="12"><path d="M0 0 H16 L0 12Z" fill="#f3f3f3"/></svg>
</aside>

<footer>
  <div class="abs footer"></div>
  <div class="abs foot-contact">LVP Roofing Kansas City, MO (555) 201-4871 / Fax (555) 201-4872<br>Email : <i>office@lvproofing.example</i></div>
  <div class="abs foot-divider"></div>
  <div class="abs foot-badge" role="img" aria-label="Limited warranty badge"></div>
  <p class="abs foot-note">We offer around the clock emergency service<br>for unexpected emergencies!</p>
  <div class="abs copyright">Copyright © 2011 LVP Network, All right reserved.</div>
</footer>

</body>
</html>
```